Webpage Toggle Button Graphics

We are a webhosting company that sells Hosted Servers (Windows/Linux etc). We have for each service in our catalogue a number of on/off/maybe toggle buttons (not actally buttons, but display). Out current design is not modern enough, and would like a new design for the concept. (current screenshot is attached).
Updates

It seems I need to clarify something.  The ICONS I need are for the Buttons in the attachment marked Anti-virus, File Backup, HIDS, DR.  Not anything else on the page. The New icons do need to fit in with the look and feel of the page, and ideally are smaller (so we can fit more of these ICONS on the page). Thanks              

Industry/Entity Type

It Company

Requirements
Must have
• Generic Button Display, with 4 states- ON (Red/Bad, I have this feature), OFF (Green/Good, I do not have this feature), N/A (greyed out, feature is not available), MAYBE (Blue, I dont have this feature but its not really Red/Bad)
• Prefer a generic version with a single visual cue (dot/button or whatever) and a Text Description (i.e. not a custom ICON for each feature)
• Needs to fit in the space similiar to the screenshot, but Ideally smaller.
• Initial buttons are to be for:
• Anti-Virus (AV)
• Backup (Back)
• Host Intrusion Detection (HIDS)
• Disaster Recovery (DR)
• DDOS (DDOS)
• Can submittions be in the format of the attachment with your designs embedded into the picture to show what it will look like in production. May Icon 1-RED, 2, Green, 3 Blue, 4 - Greyed out.
Nice to have
• Ideally the button/display is generic, and our developers can just add the text for any future buttons

```html
<!DOCTYPE html>
<html lang="en">
<head>
<meta charset="utf-8">
<title>Service Feature Status</title>
<link href="https://fonts.googleapis.com/css2?family=Arimo:wght@400;700&display=swap" rel="stylesheet">
<style>
  :root {
    --ink: #333333;
    --link: #1f5aa8;
    --row-alt: #eef1f6;
    --row-plain: #ffffff;
    --divider: #cfe0f0;
    --red: #fc3d3d;
    --green: #079869;
    --blue: #0aa0fb;
    --blue-deep: #0b66f0;
    --grey: #999999;
    --soft-top: #c2d6cf;
    --soft-bottom: #9fbcb2;
    --select-border: #a9c9e6;
  }
  * { box-sizing: border-box; margin: 0; padding: 0; }
  html, body { width: 1200px; height: 320px; overflow: hidden; background: #fff; }
  body { font-family: "Arimo", Arial, sans-serif; color: var(--ink); position: relative; }

  .header-cell { position: absolute; font-weight: 700; font-size: 13.5px; line-height: 22px; display: flex; align-items: center; gap: 3px; white-space: nowrap; }
  .sort-toggle { width: 14px; height: 14px; }
  .col-divider { position: absolute; top: 0; width: 1px; height: 320px; background: var(--divider); }

  .service-row { position: absolute; left: 0; width: 1068px; }
  .service-row.alt { background: var(--row-alt); }
  .service-row.plain { background: var(--row-plain); }

  .server-icon { position: absolute; left: 24px; width: 46px; height: 46px; }
  .service-type { position: absolute; left: 76px; font-size: 14px; white-space: nowrap; }
  .service-name { position: absolute; left: 247px; font-size: 14px; font-weight: 700; color: var(--link); line-height: 22px; white-space: nowrap; }
  .service-id { position: absolute; left: 247px; font-size: 14px; white-space: nowrap; }

  .feature { position: absolute; width: 101px; height: 30px; }
  .feature.flat { border-radius: 1px; }
  .feature.soft { border-radius: 3px; background: linear-gradient(var(--soft-top), var(--soft-bottom)); border: 1px solid #8fa9a0; }
  .feature.soft .dot { position: absolute; left: 10px; top: 6px; width: 17px; height: 17px; border-radius: 50%; }
  .feature.glossy { border-radius: 5px; border: 1px solid rgba(0,0,0,.15); }
  .feature.glossy .dot { position: absolute; left: 11px; top: 6px; width: 18px; height: 18px; border-radius: 50%; border: 1px solid rgba(255,255,255,.7); }

  .actions-select { position: absolute; left: 947px; width: 108px; height: 31px; border: 1px solid var(--select-border); border-radius: 2px; background: #fff; font-size: 14px; padding-left: 12px; line-height: 29px; }
  .actions-select .caret { position: absolute; right: 8px; top: 7px; width: 17px; height: 15px; border: 1px solid #777; background: linear-gradient(#fff, #ddd); }
  .actions-select .caret::after { content: ""; position: absolute; left: 4px; top: 5px; border-left: 4px solid transparent; border-right: 4px solid transparent; border-top: 4px solid #111; }
</style>
</head>
<body>

<svg width="0" height="0" style="position:absolute">
  <defs>
    <linearGradient id="server-fill" x1="0" y1="0" x2="0" y2="1">
      <stop offset="0" stop-color="#57c3f5"/>
      <stop offset="1" stop-color="#0b63b8"/>
    </linearGradient>
    <symbol id="server" viewBox="0 0 46 46">
      <rect x="1" y="1" width="44" height="44" rx="5" fill="url(#server-fill)" stroke="#0a5ca8"/>
      <rect x="15" y="7" width="16" height="32" fill="#e8f4fb"/>
      <rect x="18" y="11" width="10" height="2" fill="#6fb3df"/>
      <rect x="18" y="15" width="10" height="2" fill="#6fb3df"/>
      <rect x="18" y="19" width="10" height="2" fill="#6fb3df"/>
    </symbol>
    <symbol id="sort" viewBox="0 0 14 14">
      <circle cx="7" cy="7" r="6.3" fill="#fff" stroke="#5b8fd0"/>
      <path d="M4 5.5 L7 8.8 L10 5.5 Z" fill="#1d56a8"/>
    </symbol>
  </defs>
</svg>

<div class="service-row alt" style="top:52px;height:74px"></div>
<div class="service-row plain" style="top:126px;height:64px"></div>
<div class="service-row alt" style="top:190px;height:64px"></div>
<div class="service-row plain" style="top:254px;height:66px"></div>

<div class="col-divider" style="left:523px"></div>
<div class="col-divider" style="left:944px"></div>

<div class="header-cell" style="left:19px;top:27px">Service Type <svg class="sort-toggle"><use href="#sort"/></svg></div>
<div class="header-cell" style="left:247px;top:27px">Service Name <svg class="sort-toggle"><use href="#sort"/></svg></div>
<div class="header-cell" style="left:528px;top:27px">Settings <svg class="sort-toggle"><use href="#sort"/></svg></div>
<div class="header-cell" style="left:632px;top:4px">Associated</div>
<div class="header-cell" style="left:632px;top:27px">Features <svg class="sort-toggle"><use href="#sort"/></svg></div>
<div class="header-cell" style="left:831px;top:27px">Associated Features</div>
<div class="header-cell" style="left:1072px;top:15px">Actions</div>

<!-- Row 1 -->
<svg class="server-icon" style="top:68px"><use href="#server"/></svg>
<div class="service-type" style="top:70px">Virtual Managed Server</div>
<div class="service-name" style="top:57px">My New Virtual Managed Server<br>#134190</div>
<div class="service-id" style="top:105px">MIVMS7738042</div>
<div class="feature soft" style="left:526px;top:64px"><span class="dot" style="background:#d4164a"></span></div>
<div class="feature soft" style="left:631px;top:64px"><span class="dot" style="background:#0a9a3c"></span></div>
<div class="feature soft" style="left:736px;top:64px"><span class="dot" style="background:#1491f0"></span></div>
<div class="feature soft" style="left:841px;top:64px"><span class="dot" style="background:#9a9a9a"></span></div>
<div class="actions-select" style="top:67px">Actions<span class="caret"></span></div>

<!-- Row 2 -->
<svg class="server-icon" style="top:136px"><use href="#server"/></svg>
<div class="service-type" style="top:138px">Virtual Managed Server</div>
<div class="service-name" style="top:136px">Tavina_Koral_14_2</div>
<div class="service-id" style="top:160px">MIVMS7738035</div>
<div class="feature flat" style="left:526px;top:141px;background:var(--red)"></div>
<div class="feature flat" style="left:631px;top:141px;background:var(--green)"></div>
<div class="feature flat" style="left:736px;top:141px;background:var(--blue)"></div>
<div class="feature flat" style="left:841px;top:141px;background:var(--grey)"></div>
<div class="actions-select" style="top:141px">Actions<span class="caret"></span></div>

<!-- Row 3 -->
<svg class="server-icon" style="top:200px"><use href="#server"/></svg>
<div class="service-type" style="top:202px">Virtual Managed Server</div>
<div class="service-name" style="top:200px">Tavina_koral_14_1</div>
<div class="service-id" style="top:224px">MIVMS7738033</div>
<div class="feature flat" style="left:526px;top:204px;background:var(--red)"></div>
<div class="feature flat" style="left:631px;top:204px;background:var(--green)"></div>
<div class="feature flat" style="left:736px;top:204px;background:var(--blue-deep)"></div>
<div class="feature flat" style="left:841px;top:204px;background:var(--grey)"></div>
<div class="actions-select" style="top:205px">Actions<span class="caret"></span></div>

<!-- Row 4 -->
<svg class="server-icon" style="top:263px"><use href="#server"/></svg>
<div class="service-type" style="top:265px">Dedicated Server</div>
<div class="service-name" style="top:263px">Dedicated Server</div>
<div class="service-id" style="top:287px">M2DSR12821001</div>
<div class="feature glossy" style="left:527px;top:268px;background:linear-gradient(#ff7070,#e82424)"><span class="dot" style="background:radial-gradient(circle at 40% 35%,#ffb0c8,#c01250)"></span></div>
<div class="feature glossy" style="left:632px;top:268px;background:linear-gradient(#2fb585,#05855a)"><span class="dot" style="background:radial-gradient(circle at 40% 35%,#d8ffe0,#2bb050)"></span></div>
<div class="feature glossy" style="left:737px;top:268px;background:linear-gradient(#2a7fe0,#0a4fb8)"><span class="dot" style="background:radial-gradient(circle at 40% 35%,#c8f4ff,#18a0e8)"></span></div>
<div class="feature glossy" style="left:842px;top:268px;background:linear-gradient(#c4c4c4,#959595)"><span class="dot" style="background:radial-gradient(circle at 40% 35%,#ffffff,#a8a8a8)"></span></div>
<div class="actions-select" style="top:269px">Actions<span class="caret"></span></div>

</body>
</html>
```